Professional Single Page Website Design for Velloway Advisory

Velloway Advisory is a new business consultancy specializing in providing expert services to small businesses, primarily in the brick-and-mortar retail and food service sectors. We offer a range of services including franchise development and launch, due diligence, and construction management.

Currently, we have a basic website set up at www.vellowayadvisory.example, but we need a professional touch to enhance its design and functionality.

Project Requirements:
- Single Page Design: For now, we need a single page design that effectively showcases who we are, our services, and contact information.
- Future Expansion: The design should be flexible and scalable for future expansion to include additional pages like specific service offerings, about us, and a dedicated contact page.
- Design Aesthetic: We are looking for a modern yet professional design that aligns with our brand identity.
- Logo: We have a logo that we like, which was also sourced from Pixel Forum. The logo files are attached to this project brief.

Key Sections to Include:
- Hero Section: An engaging introduction to Velloway Advisory with a strong visual impact.
- About Us: A brief overview of who we are and our mission.
- Team: Section for the profiles of the two principals.
- Services: A clear and concise presentation of our services, including franchise development, due diligence, and construction management.
- Contact Information: Easy-to-find contact details, including a form for inquiries.
- Call to Action: Encouraging visitors to get in touch with us for consultations or further information.

Design Considerations:
- Ensure the design is responsive and mobile-friendly.
- Include high-quality images and icons that complement our services and industry.
- We do not need development services, this is only a design project.

```html
<!DOCTYPE html>
<html lang="en">
<head>
<meta charset="utf-8">
<title>Velloway Advisory</title>
<link rel="stylesheet" href="https://fonts.googleapis.com/css2?family=Poppins:ital,wght@0,400;0,500;0,600;0,700;0,800;1,700;1,800&display=swap">
<style>
:root{
  --ink:#222c34;
  --slate:#2b3741;
  --teal:#8fc9ae;
  --teal-deep:#6fb895;
  --teal-pale:#e7f3ed;
  --mist:#f2f3f3;
  --text:#2a2f33;
  --white:#ffffff;
}
*{box-sizing:border-box;margin:0;padding:0}
html,body{width:1200px;height:4666px;overflow:hidden}
body{font-family:"Poppins",sans-serif;color:var(--text);background:var(--white);position:relative;font-size:15px;line-height:1.62}
.abs{position:absolute}
.btn{position:absolute;display:flex;align-items:center;justify-content:center;gap:10px;font-weight:600;font-size:16px;border-radius:3px;background:var(--teal);color:var(--ink)}
.btn svg{width:18px;height:18px}
.btn.dark{background:var(--ink);color:var(--white)}
.accent{color:var(--teal)}

/* header */
.site-header{position:absolute;left:0;top:0;width:1200px;height:155px;background:var(--white)}
.brand{position:absolute;left:83px;top:52px;display:flex;align-items:center;gap:14px;font-weight:600;font-size:26px;color:var(--ink)}
.brand-dot{width:46px;height:46px;border-radius:50%;background:var(--teal)}
.nav{position:absolute;left:475px;top:64px;display:flex;gap:34px;font-size:16px;color:var(--ink)}
.header-cta{left:900px;top:50px;width:217px;height:53px}

/* hero */
.hero{position:absolute;left:0;top:155px;width:1200px;height:660px;background:linear-gradient(100deg,#27333c 0%,#2f3c46 45%,#5b6974 75%,#8d98a0 100%)}
.hero-photo{position:absolute;left:600px;top:0;width:600px;height:600px;background:radial-gradient(ellipse at 60% 40%,rgba(210,218,224,.55),rgba(60,72,82,0) 70%)}
.hero h1{position:absolute;left:83px;top:70px;width:560px;font-size:44px;line-height:1.16;font-weight:800;color:var(--white)}
.hero .tagline{position:absolute;left:83px;top:190px;font-size:27px;line-height:1.2;font-weight:800;font-style:italic;color:var(--teal)}
.hero p{position:absolute;left:83px;top:258px;width:420px;font-size:15px;line-height:1.6;color:#e6eaec}
.hero .btn{left:83px;top:452px;width:180px;height:50px}
.hero-wave{position:absolute;left:0;top:560px;width:1200px;height:260px}

/* about */
.about{position:absolute;left:0;top:800px;width:1200px;height:820px;background:var(--mist)}
.about h2{position:absolute;left:83px;top:68px;font-size:42px;font-weight:500;color:var(--ink)}
.about h2 b{font-weight:800;color:var(--teal)}
.about .copy{position:absolute;left:83px;top:128px;width:535px;font-size:15px;line-height:1.6}
.about .copy p{margin-bottom:15px}
.about .btn{left:83px;top:555px;width:176px;height:50px}
.about-photo{position:absolute;left:690px;top:80px;width:428px;height:428px;border-radius:38% 38% 38% 38%/38% 38% 38% 38%;background:linear-gradient(135deg,#8a6b52,#c8b9a7 45%,#6e5a49);transform:rotate(45deg) scale(.76)}
.about-wave{position:absolute;left:0;top:700px;width:1200px;height:130px}

/* services */
.services-title{position:absolute;left:0;top:1588px;width:1200px;text-align:center;font-size:40px;font-weight:500;color:var(--ink)}
.services-title b{font-weight:800;color:var(--teal)}
.pill{position:absolute;height:78px;border:2px solid var(--teal);border-radius:39px;display:flex;align-items:center;gap:14px;padding-left:34px;font-size:17px;line-height:1.15;color:var(--ink);background:var(--white)}
.pill svg{width:50px;height:50px;flex:none}
.pill.active{background:var(--ink);border-color:var(--ink);color:var(--white)}

.service-detail h3{position:absolute;left:83px;top:1920px;width:450px;font-size:31px;line-height:1.15;font-weight:800;color:var(--ink)}
.service-detail .copy{position:absolute;left:83px;top:1995px;width:450px;font-size:15px;line-height:1.6}
.service-detail .copy p{margin-bottom:15px}
.service-detail .btn{left:85px;top:2328px;width:176px;height:50px}
.service-art{position:absolute;left:640px;top:1920px;width:478px;height:465px;border-radius:52% 48% 44% 56%/55% 50% 50% 45%;background:linear-gradient(160deg,#eff0f0,#e3e6e5)}

/* cta band */
.cta-band{position:absolute;left:83px;top:2462px;width:1034px;height:410px;border-radius:26px;overflow:hidden;background:var(--teal)}
.cta-photo{position:absolute;left:470px;top:0;width:564px;height:410px;background:linear-gradient(90deg,var(--teal) 0%,#c9d2d0 30%,#b4b9b7 60%,#7c8684 100%)}
.cta-band h2{position:absolute;left:70px;top:58px;width:460px;font-size:39px;line-height:1.04;font-weight:800;color:var(--white)}
.cta-band p{position:absolute;left:70px;top:150px;width:430px;font-size:15px;line-height:1.6;color:var(--ink)}
.cta-band .btn{left:70px;top:295px;width:176px;height:51px}

/* team */
.team-title{position:absolute;left:0;top:2940px;width:1200px;text-align:center;font-size:40px;font-weight:500;color:var(--ink)}
.team-title b{font-weight:800;color:var(--teal)}
.member{position:absolute;width:470px;background:var(--ink);border-radius:22px;color:var(--white);text-align:center}
.member .portrait{position:absolute;left:105px;top:-130px;width:260px;height:260px;border-radius:50%;background:radial-gradient(circle at 50% 45%,#a9d6c0,var(--teal));border:6px solid var(--white)}
.member h3{position:absolute;left:0;top:160px;width:100%;font-size:30px;font-weight:700}
.member .role{position:absolute;left:0;top:200px;width:100%;font-size:19px;font-weight:700;font-style:italic;color:var(--teal)}
.member .bio{position:absolute;left:45px;top:245px;width:380px;font-size:14.5px;line-height:1.55;color:#e9eef0}
.member .bio p{margin-bottom:14px}
.contact-dots{position:absolute;left:170px;display:flex;gap:20px}
.contact-dots span{width:54px;height:54px;border-radius:50%;background:var(--teal);border:4px solid var(--white);display:flex;align-items:center;justify-content:center}
.contact-dots svg{width:22px;height:22px}

/* contact */
.contact{position:absolute;left:0;top:3890px;width:1200px;height:670px}
.contact-info{position:absolute;left:0;top:0;width:550px;height:670px;background:var(--ink)}
.contact-info ul{list-style:none;position:absolute;left:83px;top:130px;color:var(--white);font-size:16px}
.contact-info li{display:flex;gap:20px;align-items:flex-start;margin-bottom:26px}
.contact-info svg{width:18px;height:18px;flex:none;margin-top:4px}
.map{position:absolute;left:83px;top:300px;width:415px;height:232px;background:linear-gradient(135deg,#eef0ee,#dfe7e3 50%,#f1e6cf);border:2px solid var(--white)}
.contact-form{position:absolute;left:550px;top:0;width:650px;height:670px;background:linear-gradient(135deg,#9fd2bb,#8fc9ae 60%,#a9d5c1)}
.contact-form h2{position:absolute;left:50px;top:58px;font-size:38px;font-weight:800;color:var(--white)}
.field{position:absolute;height:50px;border:1.5px solid var(--ink);font-size:15px;color:var(--ink);padding:11px 14px;display:flex;align-items:flex-start;justify-content:space-between}
.field svg{width:16px;height:16px;margin-top:4px}
.contact-form .btn{left:50px;top:561px;width:140px;height:50px}

/* footer */
.site-footer{position:absolute;left:0;top:4560px;width:1200px;height:106px;background:var(--white)}
.socials{position:absolute;left:83px;top:30px;display:flex;gap:14px}
.socials span{width:48px;height:48px;border-radius:50%;background:var(--teal)}
.copyright{position:absolute;right:83px;top:42px;font-size:15px;color:var(--ink)}
</style>
</head>
<body>

<header class="site-header">
  <div class="brand"><span class="brand-dot"></span>Velloway Advisory</div>
  <nav class="nav"><span>About</span><span>Services</span><span>Our Team</span><span>Contact</span></nav>
  <a class="btn header-cta">Get Started Now <svg viewBox="0 0 20 20" fill="none" stroke="currentColor" stroke-width="1.8"><path d="M3 10h13M11 5l5 5-5 5"/></svg></a>
</header>

<section class="hero">
  <div class="hero-photo" role="img" aria-label="Photo of a hand touching a rising bar chart with an upward arrow"></div>
  <h1>Building Success in Southern California</h1>
  <div class="tagline">Expertise at Every Step:<br>From Planning to Execution</div>
  <p>At Velloway, we blend innovative strategies with local market expertise to guide your commercial real estate ventures. Whether you're launching a new restaurant, investing in retail spaces, or expanding a franchise, our dedicated team is here to turn your real estate aspirations into tangible success. Dive into a partnership that grows with you.</p>
  <a class="btn">What we do <svg viewBox="0 0 20 20" fill="none" stroke="currentColor" stroke-width="1.8"><path d="M3 10h13M11 5l5 5-5 5"/></svg></a>
  <svg class="hero-wave" viewBox="0 0 1200 260" preserveAspectRatio="none">
    <path d="M0 150 C300 230 600 260 850 180 C1000 130 1120 100 1200 110 L1200 260 L0 260Z" fill="#f2f3f3"/>
    <path d="M0 165 C300 235 600 250 850 175 C1000 130 1120 100 1200 110 L1200 120 C1120 115 1000 145 850 190 C600 265 300 250 0 180Z" fill="#8fc9ae"/>
  </svg>
</section>

<section class="about">
  <h2>About <b>Velloway Advisory</b></h2>
  <div class="copy">
    <p>Welcome to Velloway Advisory, your trusted partner in navigating the complexities of the real estate and small business markets. Founded by industry veterans Rafael Moreno and Daniel Oh, we specialize in providing comprehensive services tailored to the unique needs of our clients. Whether you're a franchisee, a new restaurant owner, or a commercial real estate investor, our expertise in due diligence, construction management, and investment property evaluation ensures you make informed, strategic decisions.</p>
    <p>At Velloway Advisory, we are committed to your success. Our approach combines meticulous analysis, strategic insights, and personalized service to help you achieve your business goals. We pride ourselves on our ability to deliver results that exceed expectations, fostering long-term relationships built on trust and excellence.</p>
    <p>Discover how Velloway Advisory can support your business journey. Partner with us and experience the difference our dedication and expertise can make.</p>
  </div>
  <a class="btn">Get Started <svg viewBox="0 0 20 20" fill="none" stroke="currentColor" stroke-width="1.8"><path d="M3 10h13M11 5l5 5-5 5"/></svg></a>
  <div class="about-photo" role="img" aria-label="Photo collage of business partners shaking hands over documents on a wooden desk"></div>
  <svg class="about-wave" viewBox="0 0 1200 130" preserveAspectRatio="none"><path d="M0 120 C250 60 500 60 800 80 C1000 95 1120 80 1200 40 L1200 130 L0 130Z" fill="#ffffff"/></svg>
</section>

<h2 class="services-title">Our <b>Services</b></h2>
<div class="pill active" style="left:123px;top:1670px;width:327px">
  <svg viewBox="0 0 50 50" fill="none" stroke="#8fc9ae" stroke-width="1.6"><circle cx="25" cy="25" r="9"/><circle cx="25" cy="25" r="18" stroke-dasharray="3 5"/><circle cx="25" cy="6" r="3"/><circle cx="25" cy="44" r="3"/><circle cx="6" cy="25" r="3"/><circle cx="44" cy="25" r="3"/></svg>
  <span>Franchise Development<br>&amp; Launch</span></div>
<div class="pill" style="left:473px;top:1670px;width:252px">
  <svg viewBox="0 0 50 50" fill="none" stroke="#8fc9ae" stroke-width="1.6"><rect x="14" y="12" width="22" height="30" rx="2"/><path d="M19 20h12M19 26h12M19 32h8"/><circle cx="12" cy="12" r="6"/><circle cx="38" cy="40" r="5"/></svg>
  <span>Due Diligence</span></div>
<div class="pill" style="left:750px;top:1670px;width:327px">
  <svg viewBox="0 0 50 50" fill="none" stroke="#8fc9ae" stroke-width="1.6"><circle cx="25" cy="22" r="12"/><path d="M13 22h24M25 10v-4M10 42h30"/><rect x="16" y="30" width="18" height="12"/></svg>
  <span>Building &amp; Construction<br>Management</span></div>
<div class="pill" style="left:300px;top:1773px;width:303px">
  <svg viewBox="0 0 50 50" fill="none" stroke="#8fc9ae" stroke-width="1.6"><path d="M8 24 25 10l17 14"/><rect x="13" y="24" width="24" height="18"/><rect x="21" y="31" width="8" height="11"/></svg>
  <span>Investment Property<br>Evaluation</span></div>
<div class="pill" style="left:627px;top:1773px;width:273px">
  <svg viewBox="0 0 50 50" fill="none" stroke="#8fc9ae" stroke-width="1.6"><circle cx="28" cy="20" r="13"/><path d="M18 29 6 41"/><path d="M22 26v-6M28 26v-10M34 26v-8"/></svg>
  <span>Market Analysis &amp;<br>Feasibility Studies</span></div>

<section class="service-detail">
  <h3>Franchise Development<br>&amp; Launch</h3>
  <div class="copy">
    <p>At Velloway Advisory, our Franchise Development &amp; Launch service is designed to transform your successful business into a thriving franchise. We start by thoroughly evaluating your business model to determine its franchisability. Once confirmed, our team handles every aspect of the franchise setup, including legal documentation, branding, marketing strategies, operational guidelines, and franchisee recruitment.</p>
    <p>Our goal is to ensure a seamless and efficient transition from a single successful location to a robust franchise network, empowering your business to scale effectively and achieve exponential growth. Partner with us to turn your business into a nationwide brand.</p>
  </div>
  <a class="btn">Get Started <svg viewBox="0 0 20 20" fill="none" stroke="currentColor" stroke-width="1.8"><path d="M3 10h13M11 5l5 5-5 5"/></svg></a>
  <div class="service-art" role="img" aria-label="Illustration of a businessman watering a tree that grows small storefronts, with a coin and stack of coins"></div>
</section>

<section class="cta-band">
  <div class="cta-photo" role="img" aria-label="Overhead photo of a team meeting around a long conference table"></div>
  <h2>Unlock Your Business Potential Today!</h2>
  <p>At Velloway Advisory, we're dedicated to turning your business aspirations into reality. Our expertise and commitment ensure you make informed, strategic decisions that drive success. Take the first step towards achieving your goals with confidence.</p>
  <a class="btn dark">Get Started <svg viewBox="0 0 20 20" fill="none" stroke="currentColor" stroke-width="1.8"><path d="M3 10h13M11 5l5 5-5 5"/></svg></a>
</section>

<h2 class="team-title">Our <b>Leadership Team</b></h2>

<article class="member" style="left:115px;top:3152px;height:563px">
  <div class="portrait" role="img" aria-label="Portrait photo of Daniel Oh"></div>
  <h3>Daniel Oh</h3>
  <div class="role">Principal</div>
  <div class="bio">
    <p>Daniel Oh is a seasoned real estate expert with extensive experience in project and construction management, and a licensed real estate agent in California. Fluent in both English and Korean, he specializes in commercial real estate, bringing invaluable expertise to Velloway Advisory.</p>
    <p>His affiliation with the National Guild of Property Brokers and the Global Forum of Retail Properties underscores his commitment to excellence and industry standards. Daniel's strategic insight and leadership in real estate development</p>
  </div>
  <div class="contact-dots" style="top:536px">
    <span><svg viewBox="0 0 24 24" fill="#fff"><path d="M6.6 10.8a15 15 0 0 0 6.6 6.6l2.2-2.2c.3-.3.7-.4 1-.2 1.1.4 2.3.6 3.6.6.6 0 1 .4 1 1V20c0 .6-.4 1-1 1A17 17 0 0 1 3 4c0-.6.4-1 1-1h3.5c.6 0 1 .4 1 1 0 1.3.2 2.5.6 3.6.1.3 0 .7-.2 1z"/></svg></span>
    <span><svg viewBox="0 0 24 24" fill="none" stroke="#fff" stroke-width="2"><rect x="3" y="5" width="18" height="14" rx="1" fill="#fff"/><path d="M3 6l9 7 9-7" stroke="#8fc9ae"/></svg></span>
  </div>
</article>

<article class="member" style="left:616px;top:3152px;height:633px">
  <div class="portrait" role="img" aria-label="Portrait photo of Rafael Moreno"></div>
  <h3>Rafael Moreno</h3>
  <div class="role">Principal</div>
  <div class="bio">
    <p>Rafael Moreno brings almost 20 years of rich experience as a real estate investor and a pivotal role at one of southern California's largest real estate management firms, sales and marketing strategies to elevate property value and investor returns. His vast expertise spans through strategic development and market analysis, making him a cornerstone for Velloway Advisory.</p>
    <p>Rafael's leadership and deep market understanding assure clients of unmatched guidance in their real estate investments, promising a partnership that drives value and innovation in every venture. Join us in transforming real estate opportunities into lasting achievements.</p>
  </div>
  <div class="contact-dots" style="top:606px">
    <span><svg viewBox="0 0 24 24" fill="#fff"><path d="M6.6 10.8a15 15 0 0 0 6.6 6.6l2.2-2.2c.3-.3.7-.4 1-.2 1.1.4 2.3.6 3.6.6.6 0 1 .4 1 1V20c0 .6-.4 1-1 1A17 17 0 0 1 3 4c0-.6.4-1 1-1h3.5c.6 0 1 .4 1 1 0 1.3.2 2.5.6 3.6.1.3 0 .7-.2 1z"/></svg></span>
    <span><svg viewBox="0 0 24 24" fill="none" stroke="#fff" stroke-width="2"><rect x="3" y="5" width="18" height="14" rx="1" fill="#fff"/><path d="M3 6l9 7 9-7" stroke="#8fc9ae"/></svg></span>
  </div>
</article>

<section class="contact">
  <div class="contact-info">
    <ul>
      <li><svg viewBox="0 0 24 24" fill="#8fc9ae"><path d="M12 2a7 7 0 0 0-7 7c0 5 7 13 7 13s7-8 7-13a7 7 0 0 0-7-7zm0 9.5A2.5 2.5 0 1 1 12 6.5a2.5 2.5 0 0 1 0 5z"/></svg><span>214 Harbor Crest Ave, Suite 5,<br>Coastview, CA 90000, USA</span></li>
      <li><svg viewBox="0 0 24 24" fill="#8fc9ae"><path d="M6.6 10.8a15 15 0 0 0 6.6 6.6l2.2-2.2c.3-.3.7-.4 1-.2 1.1.4 2.3.6 3.6.6.6 0 1 .4 1 1V20c0 .6-.4 1-1 1A17 17 0 0 1 3 4c0-.6.4-1 1-1h3.5c.6 0 1 .4 1 1 0 1.3.2 2.5.6 3.6.1.3 0 .7-.2 1z"/></svg><span>+1 (555) 014-2270</span></li>
      <li><svg viewBox="0 0 24 24" fill="#8fc9ae"><path d="M3 5h18v14H3z"/><path d="M3 6l9 7 9-7" fill="none" stroke="#222c34" stroke-width="1.6"/></svg><span>hello@vellowayadvisory.example</span></li>
    </ul>
    <div class="map" role="img" aria-label="Street map showing the office location"></div>
  </div>
  <div class="contact-form">
    <h2>Contact Us</h2>
    <div class="field" style="left:50px;top:122px;width:246px">First Name*</div>
    <div class="field" style="left:321px;top:122px;width:246px">Last Name*</div>
    <div class="field" style="left:50px;top:198px;width:517px">Company Name</div>
    <div class="field" style="left:50px;top:275px;width:246px">Phone Number*</div>
    <div class="field" style="left:321px;top:275px;width:246px">Email Address*</div>
    <div class="field" style="left:50px;top:351px;width:517px">Pick a Service <svg viewBox="0 0 16 16" fill="none" stroke="#222c34" stroke-width="1.8"><path d="M3 6l5 5 5-5"/></svg></div>
    <div class="field" style="left:50px;top:428px;width:517px;height:102px">Additional Details</div>
    <a class="btn dark">Submit <svg viewBox="0 0 20 20" fill="none" stroke="currentColor" stroke-width="1.8"><path d="M3 10h13M11 5l5 5-5 5"/></svg></a>
  </div>
</section>

<footer class="site-footer">
  <div class="socials"><span aria-label="Professional network"></span><span aria-label="Photo sharing"></span><span aria-label="Microblog"></span></div>
  <div class="copyright">© 2024 Velloway Advisory. All rights reserved.</div>
</footer>

</body>
</html>
```